need this made into a high quality editable copy...

mock this exact image and file, i created it in AI...but now i need the same thing created to where i can edit the text, add my own stuff, etc...mimic the colors, backgrounds, water, lighting, everything!

```html
<!DOCTYPE html>
<html lang="en">
<head>
<meta charset="UTF-8">
<title>The Sea Soothed My Skin – Label</title>
<link href="https://fonts.googleapis.com/css2?family=Montserrat:wght@500;700;800&display=swap" rel="stylesheet">
<style>
  :root {
    --canvas-bg: #d9dade;
    --navy-deep: #07111f;
    --navy: #0c2238;
    --ocean-mid: #1a5575;
    --ocean-teal: #1f7ea4;
    --ocean-light: #3a9cc2;
    --sky-glow: #8cc4dc;
    --sea-deep: #173f66;
    --panel-white: rgba(240, 246, 250, 0.93);
    --ink-dark: #0d1620;
    --text-light: #eef3f7;
  }
  * { margin: 0; padding: 0; box-sizing: border-box; }
  html, body { width: 1200px; height: 1000px; overflow: hidden; }
  body {
    background: var(--canvas-bg);
    font-family: "Montserrat", Arial, sans-serif;
    position: relative;
  }
  .label {
    position: absolute;
    left: 396px;
    top: 30px;
    width: 408px;
    height: 940px;
    overflow: hidden;
    background: linear-gradient(180deg,
      var(--navy-deep) 0%,
      var(--navy) 22%,
      var(--ocean-mid) 50%,
      var(--sea-deep) 62%,
      var(--ocean-teal) 86%,
      var(--ocean-light) 100%);
  }
  .label-title {
    position: absolute;
    top: 62px;
    left: 0;
    width: 100%;
    text-align: center;
    color: var(--text-light);
    font-weight: 700;
    line-height: 1;
    letter-spacing: 0.5px;
  }
  .label-title .line { display: block; font-size: 49px; margin-bottom: 6px; }
  .label-title .line-big { font-size: 68px; margin-top: 2px; }
  .scene-art {
    position: absolute;
    top: 250px;
    left: 0;
    width: 100%;
    height: 360px;
    background:
      radial-gradient(ellipse 70% 45% at 50% 48%, rgba(156, 207, 230, 0.75) 0%, rgba(156, 207, 230, 0) 70%),
      linear-gradient(180deg,
        rgba(12, 34, 56, 0) 0%,
        rgba(40, 110, 150, 0.6) 30%,
        rgba(120, 185, 215, 0.7) 55%,
        rgba(23, 63, 102, 0.95) 68%,
        rgba(23, 63, 102, 0.9) 85%,
        rgba(31, 110, 150, 0) 100%);
  }
  .feature-box {
    position: absolute;
    left: 23px;
    width: 362px;
    background: var(--panel-white);
    border-radius: 16px;
    color: var(--ink-dark);
    text-align: center;
  }
  .feature-box.headline {
    top: 585px;
    height: 156px;
    padding-top: 12px;
    font-weight: 800;
    line-height: 1.12;
  }
  .headline .kicker { display: block; font-size: 30px; }
  .headline .sub { display: block; font-size: 29px; margin-top: 8px; }
  .headline .main { display: block; font-size: 50px; margin-top: 2px; }
  .feature-box.blurb {
    top: 753px;
    height: 68px;
    padding: 10px 12px 0;
    font-weight: 500;
    font-size: 19px;
    line-height: 1.2;
  }
  .net-weight {
    position: absolute;
    top: 853px;
    left: 0;
    width: 100%;
    text-align: center;
    color: var(--text-light);
    font-weight: 500;
    font-size: 23px;
  }
</style>
</head>
<body>
  <main class="label">
    <h1 class="label-title">
      <span class="line">THE SEA</span>
      <span class="line">SOOTHED MY</span>
      <span class="line line-big">SKIN</span>
    </h1>
    <div class="scene-art" role="img" aria-label="Illustration of a lightning bolt over clouds and a deep blue ocean horizon"></div>
    <div class="feature-box headline">
      <span class="kicker">PRODUCT FEATURE</span>
      <span class="sub">THE SEA SOOTHED</span>
      <span class="main">MY SKIN</span>
    </div>
    <p class="feature-box blurb">Lorem ipsum dolor sit amet, con-<br>sectetuer adipiscing elit, sed dia</p>
    <p class="net-weight">Net. 4 OZ (118 ml)</p>
  </main>
</body>
</html>
```